hi all

Im after a new age looking business card with my company logo on it

must include these details, I would like the PH and Email to be symbols

If the colours used for card could be kept within the colours used in logo that I have supplied that would be great, if another colour is to be used dark grey would be ok. no light bulbs etc thanks

Details below to be incorporated on card

Damian Holloway

Lic E871302

PH 0219647381

E info@brightvaleelectrical.example.nz

Domestic Commercial Industrial Electricians

```html
<!DOCTYPE html>
<html lang="en">
<head>
<meta charset="utf-8">
<title>Brightvale Electrical – Business Card</title>
<link rel="stylesheet" href="https://fonts.googleapis.com/css2?family=Montserrat:wght@400;500;700&display=swap">
<style>
  :root {
    --page: #eeeeee;
    --card-light: #3a3a3a;
    --card-dark: #222222;
    --brand-blue: #1a78c2;
    --icon-blue: #3aaee0;
    --band-top: #8a8a90;
    --band-bottom: #67676c;
    --icon-disc: #2a2a2b;
    --text-light: #f2f2f2;
    --text-muted: #8c8c8c;
  }
  * { margin: 0; padding: 0; box-sizing: border-box; }
  html, body { width: 1200px; height: 1200px; overflow: hidden; }
  body {
    background: var(--page);
    font-family: "Montserrat", sans-serif;
    position: relative;
  }
  .card {
    position: absolute;
    background: radial-gradient(circle at 72% 18%, var(--card-light) 0%, var(--card-dark) 62%);
    overflow: hidden;
  }
  .card-front { left: 258px; top: 115px; width: 750px; height: 429px; }
  .card-back  { left: 257px; top: 671px; width: 758px; height: 433px; }

  .brand-mark {
    position: absolute;
    border-radius: 50%;
    border: 3px solid var(--brand-blue);
  }
  .brand-name {
    position: absolute;
    color: var(--brand-blue);
    font-weight: 700;
    letter-spacing: 0.03em;
    white-space: nowrap;
    text-transform: uppercase;
  }
  .card-front .brand-mark { left: 152px; top: 244px; width: 86px; height: 86px; }
  .card-front .brand-name { left: 60px; top: 343px; font-size: 22px; }

  .card-back .brand-mark { left: 108px; top: 39px; width: 48px; height: 48px; }
  .card-back .brand-name { left: 55px; top: 95px; font-size: 12.5px; }

  .contact-band {
    position: absolute;
    left: 652px; top: 0;
    width: 47px; height: 388px;
    border-radius: 0 0 24px 24px;
    background: linear-gradient(to bottom, var(--band-top), var(--band-bottom));
  }
  .contact-icon {
    position: absolute;
    left: 658px;
    width: 36px; height: 36px;
    border-radius: 50%;
    background: var(--icon-disc);
    display: flex; align-items: center; justify-content: center;
  }
  .contact-icon svg { width: 18px; height: 18px; fill: var(--icon-blue); }
  .contact-text {
    position: absolute;
    right: 124px;
    color: var(--text-light);
    font-size: 15.5px;
    font-weight: 500;
    letter-spacing: 0.01em;
    white-space: nowrap;
    line-height: 20px;
  }
  .contact-phone { top: 230px; }
  .contact-email { top: 282px; }
  .contact-web   { top: 335px; }
  .icon-phone { top: 222px; }
  .icon-email { top: 274px; }
  .icon-web   { top: 327px; }

  .holder-name {
    position: absolute;
    left: 46px; top: 320px;
    color: var(--brand-blue);
    font-size: 28px;
    font-weight: 700;
    letter-spacing: 0.02em;
    white-space: nowrap;
  }
  .holder-role {
    position: absolute;
    left: 47px; top: 362px;
    color: var(--text-muted);
    font-size: 15.5px;
    font-weight: 500;
    white-space: nowrap;
  }
  .holder-licence {
    position: absolute;
    left: 47px; top: 386px;
    color: var(--text-muted);
    font-size: 13px;
    font-weight: 500;
    letter-spacing: 0.03em;
    white-space: nowrap;
  }
</style>
</head>
<body>
  <section class="card card-front" aria-label="Card front">
    <div class="brand-mark" aria-hidden="true"></div>
    <div class="brand-name">Brightvale Electrical</div>
  </section>

  <section class="card card-back" aria-label="Card back">
    <div class="brand-mark" aria-hidden="true"></div>
    <div class="brand-name">Brightvale Electrical</div>

    <div class="contact-band" aria-hidden="true"></div>

    <div class="contact-text contact-phone">021 9647381</div>
    <div class="contact-icon icon-phone">
      <svg viewBox="0 0 24 24" aria-label="Phone"><path d="M3 8c0-2 4-4 9-4s9 2 9 4v2h-5V8H8v2H3z"/><path d="M7 11h10l3 8H4z"/><circle cx="12" cy="15" r="2.2" fill="#2a2a2b"/></svg>
    </div>

    <div class="contact-text contact-email">info@brightvaleelectrical.example.nz</div>
    <div class="contact-icon icon-email">
      <svg viewBox="0 0 24 24" aria-label="Email"><path d="M2 6h20v12H2z"/><path d="M2 6l10 7 10-7" fill="none" stroke="#2a2a2b" stroke-width="1.6"/><path d="M2 18l8-6M22 18l-8-6" fill="none" stroke="#2a2a2b" stroke-width="1.4"/></svg>
    </div>

    <div class="contact-text contact-web">www.brightvale.example.com</div>
    <div class="contact-icon icon-web">
      <svg viewBox="0 0 24 24" aria-label="Website"><circle cx="12" cy="12" r="10"/><g fill="none" stroke="#2a2a2b" stroke-width="1.2"><ellipse cx="12" cy="12" rx="4.5" ry="10"/><path d="M2 12h20M12 2v20M4 7h16M4 17h16"/></g></svg>
    </div>

    <div class="holder-name">DAMIAN HOLLOWAY</div>
    <div class="holder-role">Domestic Commercial Industrial Electricians</div>
    <div class="holder-licence">Lic E871302</div>
  </section>
</body>
</html>
```